First CD Cover for Independent Piano Artist

I need a CD cover design for my reflective, inspirational songs at the piano. The title will be one of the song tracks, "Wake, Bright Lantern," which will appear on the front along with my name, Marla Venton. Since I plan to produce my CD with PressBay, the design template to use is here: https://www.pressbay-example.com/templates/ecowallets.asp - it's the fourth option, 4 Panel Eco-Wallet w/ Spine. Jewel Box Size (W139).
Updates

Thank you for your artistic submissions. After some collaboration, the title of the album is changing to one of the song titles, "Wake, Bright Lantern." The visual imagery will need to shift as well. Please see the updates in the brief. I will make this a guaranteed contest for the inconvenience. Thank you again.

Industry/Entity Type

Christian

Requirements
Must have
• FRONT: Please incorporate in a creative way the attached image which I made. Use at least the woman flying (cage is optional). Ok to make edits, change the colors, textures, etc. BACK: I would like to include a photo of myself and the five track titles on the back cover, and my logo (Marla Venton Music). The photos are attached. INSIDE: Open for ideas here. I do have some text to include.
Nice to have
• I love art that looks like it has texture! Feel free to use one or more of these ideas: nature or landscape elements, musical elements, piano keys, watercolors, collage style. The mood should be beautiful and serene, yet also intriguing and passionate.
Should not have
• I don't like monochrome or grayscale for this project.

```html
<!DOCTYPE html>
<html lang="en">
<head>
<meta charset="utf-8">
<title>Wake, Bright Lantern · Marla Venton · Eco-Wallet Layout</title>
<link rel="stylesheet" href="https://fonts.googleapis.com/css2?family=Fascinate&family=Cinzel+Decorative:wght@700&display=swap">
<style>
  :root {
    --board: #2f3c4a;
    --spine: #1a2230;
    --gold: #f0bb3e;
    --deep-sea: #0b2a4a;
    --ghost: #27323e;
    --ghost-line: #3e4c5b;
    --track: #e9f0f6;
    --fold: #f4f6f8;
  }
  * { box-sizing: border-box; margin: 0; padding: 0; }
  html, body { width: 802px; height: 1200px; overflow: hidden; }
  body { background: var(--board); position: relative; }

  .panel { position: absolute; overflow: hidden; }
  .artwork { position: absolute; inset: 0; }

  /* Outer spread */
  .back-cover { left: 45px; top: 48px; width: 430px; height: 305px; }
  .back-cover .artwork {
    background:
      radial-gradient(ellipse 60% 30% at 30% 78%, rgba(170,215,240,.55) 0%, rgba(170,215,240,0) 70%),
      radial-gradient(ellipse 80% 40% at 10% 95%, #0a3a66 0%, rgba(10,58,102,0) 70%),
      linear-gradient(180deg, #0e2f52 0%, #1a4f7c 40%, #2f77a8 62%, #0f3a62 80%, #081f38 100%);
  }
  .spine { left: 475px; top: 48px; width: 30px; height: 305px; background: var(--spine); }
  .front-cover { left: 505px; top: 48px; width: 257px; height: 305px; }
  .front-cover .artwork {
    background:
      radial-gradient(ellipse 35% 30% at 62% 28%, rgba(240,250,255,.95) 0%, rgba(200,230,250,.6) 40%, rgba(200,230,250,0) 100%),
      radial-gradient(ellipse 70% 28% at 50% 92%, #1a2530 0%, rgba(26,37,48,0) 80%),
      radial-gradient(ellipse 60% 35% at 20% 70%, rgba(40,90,130,.8) 0%, rgba(40,90,130,0) 80%),
      linear-gradient(180deg, #1c4a78 0%, #5d9cc9 35%, #3b78a8 60%, #16344f 100%);
  }

  /* Inner spread */
  .inside-left { left: 45px; top: 395px; width: 365px; height: 380px; }
  .inside-left .artwork {
    background:
      radial-gradient(ellipse 70% 25% at 40% 72%, rgba(170,215,240,.5) 0%, rgba(170,215,240,0) 70%),
      linear-gradient(180deg, #123a60 0%, #1c5c8a 40%, #2c74a6 62%, #0f3a62 80%, #081f38 100%);
  }
  .inside-fold { left: 410px; top: 395px; width: 22px; height: 380px; background: var(--fold); }
  .inside-right { left: 432px; top: 395px; width: 330px; height: 380px; }
  .inside-right .artwork {
    background:
      radial-gradient(ellipse 35% 25% at 70% 20%, rgba(200,230,250,.55) 0%, rgba(200,230,250,0) 100%),
      radial-gradient(ellipse 70% 30% at 55% 90%, #121c26 0%, rgba(18,28,38,0) 80%),
      linear-gradient(180deg, #123454 0%, #2a6a9a 40%, #1a4a74 65%, #0a2540 100%);
  }

  .title {
    position: absolute; font-family: "Fascinate", cursive; font-weight: 400;
    color: var(--gold); text-transform: lowercase; line-height: .95; white-space: nowrap;
  }
  .title .sub { display: block; font-size: .5em; }
  .artist {
    position: absolute; font-family: "Cinzel Decorative", serif; font-weight: 700;
    color: var(--gold); line-height: 1; white-space: nowrap;
  }

  .back-cover .title { left: 16px; top: 14px; font-size: 40px; }
  .back-cover .artist { left: 18px; top: 84px; font-size: 14px; }
  .portrait { position: absolute; left: 16px; top: 108px; width: 130px; height: 112px;
    background: linear-gradient(160deg, #6f8a6b 0%, #3b5a3f 50%, #1f3a44 100%); }

  .tracklist { position: absolute; left: 185px; top: 22px; list-style: none;
    font-family: "Cinzel Decorative", serif; font-weight: 700; font-size: 13px; color: var(--track); }
  .tracklist li { height: 29px; }

  .spine-text { position: absolute; left: 50%; top: 14px; transform: translateX(-50%);
    writing-mode: vertical-rl; white-space: nowrap; display: flex; gap: 10px; align-items: center; }
  .spine-title { font-family: "Fascinate", cursive; color: var(--gold); font-size: 12px; text-transform: lowercase; }
  .spine-artist { font-family: "Cinzel Decorative", serif; font-weight: 700; color: var(--gold); font-size: 10px; }

  .front-cover .title { left: 18px; top: 172px; font-size: 50px; }
  .front-cover .artist { left: 50px; top: 264px; font-size: 16px; }

  .inside-left .title { left: 26px; top: 104px; font-size: 56px; }
  .inside-left .artist { left: 60px; top: 208px; font-size: 18px; }

  /* Wordmark */
  .wordmark { position: absolute; left: 40px; top: 820px; width: 300px; height: 330px; }
  .ghost-title {
    position: absolute; left: 0; top: 0; height: 320px;
    font-family: "Fascinate", cursive; font-size: 60px; line-height: .95;
    color: var(--ghost); -webkit-text-stroke: 2px var(--ghost-line);
    writing-mode: vertical-rl; transform: rotate(180deg);
    text-transform: lowercase; white-space: nowrap;
  }
  .ghost-title span { display: block; }
  .wordmark .artist { left: 200px; top: 20px; height: 290px; font-size: 24px;
    writing-mode: vertical-rl; transform: rotate(180deg); }

  /* Disc */
  .disc { position: absolute; left: 467px; top: 841px; width: 294px; height: 294px; border-radius: 50%;
    background: var(--board); box-shadow: 0 0 0 2px #46566a; }
</style>
</head>
<body>

  <section class="panel back-cover">
    <div class="artwork" role="img" aria-label="Stormy ocean wave with floating bubbles"></div>
    <h2 class="title">wake,<span class="sub">bright lantern</span></h2>
    <p class="artist">Marla Venton</p>
    <div class="portrait" role="img" aria-label="Photo of the artist seated outdoors"></div>
    <ol class="tracklist">
      <li>1. Song Name</li>
      <li>2. Song Name</li>
      <li>3. Song Name</li>
      <li>4. Song Name</li>
      <li>5. Song Name</li>
    </ol>
  </section>

  <section class="panel spine">
    <div class="spine-text">
      <span class="spine-title">wake, bright lantern</span>
      <span class="spine-artist">Marla Venton</span>
    </div>
  </section>

  <section class="panel front-cover">
    <div class="artwork" role="img" aria-label="Woman in a white gown flying above a stormy sea under lightning"></div>
    <h1 class="title">wake,<span class="sub">bright lantern</span></h1>
    <p class="artist">Marla Venton</p>
  </section>

  <section class="panel inside-left">
    <div class="artwork" role="img" aria-label="Crashing ocean wave with bubbles"></div>
    <h2 class="title">wake,<span class="sub">bright lantern</span></h2>
    <p class="artist">Marla Venton</p>
  </section>
  <div class="panel inside-fold"></div>
  <section class="panel inside-right">
    <div class="artwork" role="img" aria-label="Dark stormy sea with a faint figure in flight"></div>
  </section>

  <div class="wordmark">
    <p class="ghost-title"><span>wake,</span><span>bright</span><span>lantern</span></p>
    <p class="artist">Marla Venton</p>
  </div>

  <svg class="disc" viewBox="0 0 294 294" role="img" aria-label="Disc printed with the flying woman over the stormy sea">
    <defs>
      <radialGradient id="disc-sky" cx="62%" cy="30%" r="75%">
        <stop offset="0" stop-color="#eef8ff"/>
        <stop offset="0.25" stop-color="#8ec3e6"/>
        <stop offset="0.6" stop-color="#2f6d9e"/>
        <stop offset="1" stop-color="#0b2a4a"/>
      </radialGradient>
      <radialGradient id="disc-rock" cx="50%" cy="100%" r="55%">
        <stop offset="0" stop-color="#1a2530"/>
        <stop offset="1" stop-color="#1a2530" stop-opacity="0"/>
      </radialGradient>
    </defs>
    <circle cx="147" cy="147" r="147" fill="url(#disc-sky)"/>
    <circle cx="147" cy="147" r="147" fill="url(#disc-rock)"/>
    <circle cx="147" cy="147" r="52" fill="#c9ccd1"/>
    <circle cx="147" cy="147" r="22" fill="var(--board)"/>
  </svg>

</body>
</html>
```